Veteran Owned General Contractor needs Bold New Business Cards

We are a service disabled veteran owned small business. We're a general contractor that specializes in excavation, underground utilities, site work, land clearing and demolition. We would like a fresh, simple, bold, new look for our business cards. We're open to ideas! We'd like to incorporate the following information on the card:

Company Name & Logo, Name of Person, Job Title, Office Phone, Fax, Cell Phone, Email Address, Website, SDVOSB

Our logo is included. We look forward to your thoughts.

Thank you!
Updates

Reason: Hello Due to the overwhelming response to this project, we are extending the deadline one time to allow for improved communication and feedback with the top candidates. We would like to thank everyone for their hard work and exceptional creativity! Thank you

Industry/Entity Type

Business

Contact Information for Business Card

Font styles to use
Sans Serif

Requirements
Nice to have
• As we are a veteran owned company, it would be nice to incorporate an American flag into the design. Maybe on the back?

```html
<!DOCTYPE html>
<html lang="en">
<head>
<meta charset="utf-8">
<title>Ridgeline Co – Business Card</title>
<link rel="stylesheet" href="https://fonts.googleapis.com/css2?family=Saira:wght@400;600;700&display=swap">
<style>
  :root {
    --page: #ffffff;
    --card: #000000;
    --rim: #808184;
    --green: #6dbe45;
    --ink: #ffffff;
  }
  html, body {
    margin: 0;
    padding: 0;
    width: 1200px;
    height: 1200px;
    overflow: hidden;
    background: var(--page);
  }
  .sheet { display: block; width: 1200px; height: 1200px; }
  .card-rim { fill: var(--rim); }
  .card-face { fill: var(--card); }
  .brand-square { fill: none; stroke: var(--rim); }
  .brand-name { fill: var(--green); font-family: "Saira", sans-serif; font-weight: 700; }
  .person-name { fill: var(--green); font-family: "Saira", sans-serif; font-weight: 600; font-size: 48px; }
  .info { fill: var(--ink); font-family: "Saira", sans-serif; font-weight: 400; }
  .info-lg { font-size: 34px; }
  .info-md { font-size: 31px; }
  .tagline { fill: var(--ink); font-family: "Saira", sans-serif; font-weight: 400; font-size: 24px; }
  .icon { fill: var(--green); }
  .icon-line { fill: none; stroke: var(--green); stroke-width: 2; }
</style>
</head>
<body>
<svg class="sheet" viewBox="0 0 1500 1500" xmlns="http://www.w3.org/2000/svg">
  <defs>
    <g id="card-shape">
      <path class="card-rim" d="M240,105 Q750,39 1260,105 Q1272,110 1276,125 Q1370,400 1276,672 Q1272,686 1260,690 Q750,756 240,690 Q228,686 224,672 Q130,400 224,125 Q228,110 240,105 Z"/>
      <path class="card-face" d="M252,124 Q750,60 1248,124 Q1256,128 1259,138 Q1345,400 1259,660 Q1256,670 1248,672 Q750,736 252,672 Q244,670 241,660 Q155,400 241,138 Q244,128 252,124 Z"/>
    </g>
  </defs>

  <g class="card card-front">
    <use href="#card-shape"/>
    <rect class="brand-square" x="324" y="192" width="258" height="258" rx="22" stroke-width="12"/>
    <text class="brand-name" x="280" y="525" font-size="44" textLength="345" lengthAdjust="spacingAndGlyphs">RIDGELINE CO</text>

    <g class="web">
      <circle class="icon-line" cx="287" cy="591" r="12"/>
      <ellipse class="icon-line" cx="287" cy="591" rx="5" ry="12"/>
      <line class="icon-line" x1="275" y1="591" x2="299" y2="591"/>
      <text class="info info-md" x="317" y="603">www.ridgelineco.com</text>
    </g>

    <text class="person-name" x="710" y="233">Name Here</text>
    <text class="info info-md" x="710" y="274">Position</text>

    <g class="contact-lines">
      <rect class="icon-line" x="716" y="323" width="20" height="34" rx="3" stroke-width="3"/>
      <text class="info info-lg" x="758" y="352">(000) 000-0000</text>

      <path class="icon" d="M716,370 q6,-4 9,2 l2,6 q0,4 -4,5 q2,8 10,14 q3,-3 6,-1 l4,4 q2,4 -3,7 q-8,3 -16,-10 q-10,-15 -8,-27 Z"/>
      <text class="info info-lg" x="758" y="396">(555) 014-2288</text>

      <rect class="icon" x="709" y="424" width="34" height="20"/>
      <rect class="icon" x="717" y="414" width="20" height="10"/>
      <rect class="card-face" x="724" y="428" width="14" height="12"/>
      <text class="info info-lg" x="758" y="440">(000) 000-0000</text>

      <rect class="icon" x="711" y="467" width="31" height="19"/>
      <path d="M711,467 L726,479 L742,467" fill="none" stroke="#000" stroke-width="2"/>
      <text class="info info-lg" x="760" y="484">office@ridgelineco.com</text>
    </g>

    <text class="info info-lg" x="710" y="559">4820 NE Cedar Ct</text>
    <text class="info info-lg" x="710" y="604">Fairview, OR 97024</text>
  </g>

  <g class="card card-back" transform="translate(0,700)">
    <use href="#card-shape"/>
    <rect class="brand-square" x="355" y="317" width="110" height="110" rx="12" stroke-width="6"/>
    <text class="brand-name" x="490" y="405" font-size="96" textLength="660" lengthAdjust="spacingAndGlyphs">RIDGELINE CO</text>
    <text class="tagline" x="750" y="481" text-anchor="middle">Residential Construction | Commercial Construction | Clearing &amp; Demolition</text>
  </g>
</svg>
</body>
</html>
```